VerdaTurf - 11" x 4" Door Hanger, full color both sides

We need a door hanger designed, 11" x 4", full color both sides, We are a lawn care company that provides lawn mowing, and other services to clients. This door hanger will be place on the 9 neighbors of our current clients. The ad needs to state that we provided lawn service to one of their neighbors today, and that we are in their neighborhood each week on that day. The door hanger will have 4 printings, substituting the day of Tuesday, Wednesday, Thursday, and Friday. All the art work and text will remain the same except the day of the week. For information about VerdaTurf, please visit our website www.verdaturf-example.net. The main emphasis of the message should be that we are their every week on that day, and the benefits to them of using our service (ie. quality time with their family, golf, sports, resting, etc., instead of mowing the lawn). At the bottom of the door hanger will be a coupon offering their tenth (10th) lawn service free, which is the same as a 10% discount.

I have uploaded a template files for the front and back of an 11 x 4 door hanger, The templates are pdf, jpeg, or eps files. The final product can be a pdf, jpeg, or eps file.

Target Market(s)

Neighbors of our existing clients

Industry/Entity Type

Lawn Care

Font styles to use
Serif

Requirements
Must have
• Professional design and art, Short conversational message that relays the following thoughts:
• 1. We mowed your neighbor's lawn today!
• 2. We are in your neighborhood every Tuesday!
• 3. Our lawn service is guaranteed.
• 4. Call to action - Call us today! 512-748-3091
• 5. Of course our contact info, name, phone number, website address.
• 6. Coupon at bottom for "10th lawn service Free!"
Nice to have
• Art work from our website is fine to use, That carries our theme throughout our campaign.
Should not have
• Very wordy. This is basically a billboard, Have very few seconds to grab their attention.

```html
<!DOCTYPE html>
<html lang="en">
<head>
<meta charset="utf-8">
<title>VerdaTurf Door Hanger</title>
<link rel="stylesheet" href="https://fonts.googleapis.com/css2?family=Montserrat:wght@500;600;700&family=Oswald:wght@400;500;600;700&display=swap">
<style>
  :root {
    --stage: #d9d9d9;
    --red: #e8434a;
    --red-deep: #d8343b;
    --ink: #141414;
    --black-band: #1e1e1e;
    --white: #ffffff;
    --sky-top: #d6ebfa;
    --sky-mid: #eef7fd;
    --grass: #5aa73a;
    --grass-dark: #2f6b22;
  }
  * { box-sizing: border-box; margin: 0; padding: 0; }
  html, body { width: 938px; height: 1200px; overflow: hidden; }
  body {
    background: var(--stage);
    font-family: "Montserrat", sans-serif;
    position: relative;
  }
  .hanger {
    position: absolute;
    top: 95px;
    width: 420px;
    height: 1010px;
    background: var(--white);
    overflow: hidden;
  }
  .hanger--front { left: 34px; }
  .hanger--back { left: 484px; }

  .sky {
    position: absolute; left: 0; top: 0; width: 100%; height: 560px;
    background: radial-gradient(ellipse at 50% 40%, var(--white) 0%, var(--sky-mid) 45%, var(--sky-top) 100%);
  }
  .slit {
    position: absolute; left: 0; top: 168px; width: 210px; height: 22px;
    background: var(--stage);
  }
  .hole {
    position: absolute; left: 164px; top: 134px; width: 92px; height: 92px;
    border-radius: 50%; background: var(--stage);
  }
  .web {
    position: absolute; left: 0; width: 100%; text-align: center;
    font-weight: 700; font-size: 22px; color: var(--ink);
  }
  .web em { font-style: normal; color: var(--red); }
  .brand {
    position: absolute; left: 0; width: 100%; text-align: center;
    font-weight: 500; font-size: 36px; letter-spacing: 3px; color: var(--ink);
  }
  .photo { position: absolute; left: 0; width: 100%; }
  .photo--house {
    top: 294px; height: 250px;
    background: linear-gradient(180deg, #9fcdf0 0%, #d9e6ef 35%, #d8cfb4 50%, #6fa84a 70%, var(--grass) 100%);
  }
  .photo--family {
    top: 340px; height: 240px;
    background: linear-gradient(180deg, #22401f 0%, #2f5a28 55%, #4f8f34 80%, var(--grass) 100%);
  }
  .band-red {
    position: absolute; left: 0; width: 100%;
    background: linear-gradient(180deg, var(--red) 0%, var(--red-deep) 100%);
  }
  .front-band { top: 535px; height: 160px; }
  .headline {
    position: absolute; left: 0; top: 558px; width: 100%; text-align: center;
    color: var(--white); font-weight: 600; line-height: 1.18;
  }
  .headline .small { font-size: 23px; display: block; }
  .headline .big { font-size: 30px; display: block; }

  .badge {
    position: absolute; left: 32px; top: 670px; width: 168px; height: 168px;
    border-radius: 50%; background: var(--ink); border: 6px solid var(--white);
    display: flex; flex-direction: column; align-items: center; justify-content: center;
    font-family: "Oswald", sans-serif; line-height: 1.15; text-align: center;
  }
  .badge .w { color: var(--white); font-size: 17px; font-weight: 400; }
  .badge .r { color: var(--red); font-size: 20px; font-weight: 500; }
  .badge .day { color: var(--red); font-size: 28px; font-weight: 700; }

  .call {
    position: absolute; left: 210px; top: 712px; width: 190px; text-align: center;
    font-family: "Oswald", sans-serif;
  }
  .call .lead { font-size: 22px; color: var(--ink); font-weight: 500; display: block; }
  .call .phone { font-size: 29px; color: var(--red); font-weight: 500; display: block; margin-top: 2px; }

  .grass-strip {
    position: absolute; left: 0; top: 805px; width: 100%; height: 65px;
    background: linear-gradient(180deg, #8fd35a 0%, var(--grass) 50%, var(--grass-dark) 100%);
  }

  .coupon {
    position: absolute; left: 0; top: 870px; width: 100%; height: 140px;
    background: var(--black-band);
    border-top: 2px dashed #bdbdbd;
    text-align: center; color: var(--white);
  }
  .coupon .c-brand {
    display: block; margin-top: 18px; font-size: 14px; font-weight: 500; letter-spacing: 1px;
  }
  .coupon .offer {
    display: flex; justify-content: center; align-items: center; gap: 8px; margin-top: 6px;
  }
  .coupon .red-word {
    font-family: "Oswald", sans-serif; font-weight: 600; color: var(--red); font-size: 52px; line-height: 1;
  }
  .coupon .red-word sub { font-size: 34px; vertical-align: baseline; }
  .coupon .stack { display: flex; flex-direction: column; line-height: 1; text-align: left; }
  .coupon .stack .l1 { font-size: 25px; font-weight: 600; }
  .coupon .stack .l2 { font-size: 18px; font-weight: 600; }
  .scissors { position: absolute; left: 8px; top: -11px; }

  .promise {
    position: absolute; left: 0; top: 232px; width: 100%; text-align: center;
    font-family: "Oswald", sans-serif; line-height: 1;
  }
  .promise .lead { display: block; font-size: 30px; font-weight: 500; color: var(--ink); }
  .promise .big { display: block; font-size: 62px; font-weight: 700; color: var(--red); margin-top: 6px; }

  .back-band { top: 578px; height: 200px; }
  .about {
    position: absolute; left: 56px; top: 596px; width: 308px; color: var(--white);
    font-family: "Oswald", sans-serif;
  }
  .about h2 {
    text-align: center; color: var(--ink); font-size: 28px; font-weight: 500; margin-bottom: 8px;
  }
  .about p { font-size: 11.5px; line-height: 1.5; font-weight: 400; }
  .pill {
    position: absolute; left: 58px; top: 722px; width: 302px; height: 46px;
    background: var(--ink); color: var(--white); border-radius: 12px;
    font-family: "Oswald", sans-serif; font-size: 24px; font-weight: 500;
    display: flex; align-items: center; justify-content: center;
  }
  .white-foot {
    position: absolute; left: 0; top: 778px; width: 100%; height: 92px; background: var(--white);
  }
</style>
</head>
<body>

<section class="hanger hanger--front">
  <div class="sky"></div>
  <p class="web" style="top:72px">www.<em>verdaturf-example</em>.net</p>
  <div class="slit"></div>
  <div class="hole"></div>
  <h1 class="brand" style="top:238px">VERDATURF</h1>
  <div class="photo photo--house" role="img" aria-label="Photo of a tidy house with a freshly mowed front lawn and a paved path"></div>
  <div class="band-red front-band"></div>
  <p class="headline">
    <span class="small">We mowed your</span>
    <span class="big">Neighbor's lawn</span>
    <span class="big">Today!</span>
  </p>
  <div class="grass-strip" role="img" aria-label="Illustration of green grass blades"></div>
  <div class="badge">
    <span class="w">We are in your</span>
    <span class="r">Neighborhood</span>
    <span class="w">Every</span>
    <span class="day">Tuesday!</span>
  </div>
  <p class="call">
    <span class="lead">Call us today!</span>
    <span class="phone">512-748-3091</span>
  </p>
  <div class="coupon">
    <span class="c-brand">VERDATURF</span>
    <div class="offer">
      <span class="red-word">10<sub>th</sub></span>
      <span class="stack"><span class="l1">Lawn</span><span class="l2">Service</span></span>
      <span class="red-word">Free</span>
    </div>
  </div>
</section>

<section class="hanger hanger--back">
  <div class="sky"></div>
  <h1 class="brand" style="top:68px">VERDATURF</h1>
  <div class="slit"></div>
  <div class="hole"></div>
  <h2 class="promise">
    <span class="lead">Our Lawn Service is</span>
    <span class="big">Guaranteed</span>
  </h2>
  <div class="photo photo--family" role="img" aria-label="Photo of a family playing with balloons on a green lawn"></div>
  <div class="band-red back-band"></div>
  <div class="about">
    <h2>About Us</h2>
    <p>VerdaTurf is a family owned company. VerdaTurf's mission is to bring service excellence to our client. Our goal is to provide this service excellence in our administrative areas, as well as in the field operations.</p>
  </div>
  <div class="pill">Call us today! 512-748-3091</div>
  <div class="white-foot"></div>
  <p class="web" style="top:830px">www.verdaturf-example.net</p>
  <div class="coupon">
    <svg class="scissors" width="30" height="20" viewBox="0 0 30 20" aria-hidden="true">
      <circle cx="5" cy="5" r="4" fill="none" stroke="#ffffff" stroke-width="2"/>
      <circle cx="5" cy="15" r="4" fill="none" stroke="#ffffff" stroke-width="2"/>
      <line x1="8" y1="7" x2="28" y2="15" stroke="#ffffff" stroke-width="2"/>
      <line x1="8" y1="13" x2="28" y2="5" stroke="#ffffff" stroke-width="2"/>
    </svg>
    <span class="c-brand">VERDATURF</span>
    <div class="offer">
      <span class="red-word">10<sub>th</sub></span>
      <span class="stack"><span class="l1">Lawn</span><span class="l2">Service</span></span>
      <span class="red-word">Free</span>
    </div>
  </div>
</section>

</body>
</html>
```